BRAVOLK PROMOTION GROUP Website

Looking for a website design that clearly and powerfully portrays our unique and effective indoor advertising billboards in our network.

Our TeenyPanels, LargoPanels and TitanFlags are strategically placed in high traffic areas of restaurants, pubs, nightclubs, fitness clubs, colleges and universities, and sports arenas.

Bravolk Promotion Group is our new name. Our current site is www.plorvex.ca with our focus now being entirely on our Out-of-Home media. New website address will be www.bravolkpromotion.ca

We need the following sections:

HOME
PRODUCTS (Drop down menu)
-TeenyPanels
-LargoPanels
-TitanFlags
NETWORKS (Drop down menu)
-Resto-Bar
-Sports
-Campus
EFFECTIVENESS
CAMPAIGNS *This page will show numerous ad campaigns and could be a slide show (see www.plorvex.ca/QJPV_campaigns.html )
BECOME A PARTNER
CONTACT

Please include social media functions on the homepage such as chirpnet/visagebook/workloop

We will be supplying content and photos as required.

Our plan is to have you submit the homepage design to start with, and then we can start judging which styles we like the best and can start narrowing our list. As a second round, we would like to ask the "finalists" to submit a second page (another section of the website) and to see how consistent you are in terms of the look and feel you proposed for the homepage.

Attached is our new logo.

We may require you to upload the final website for us.

Websites that are in similar industry are:
www.trelmuk.com
www.quasplen.com

Industry/Entity Type

Advertising

Requirements
Must have
• Our network offers advertising solutions that feature: Guaranteed Readership,100% Gender Specific, Frequency, and Captive Audience. Purchasing advertising space in our network are small to medium business owners and advertising agencies booking on behalf of their clients.

Site must be professional and modern looking.
Nice to have
• Moving banner or slide show of some type.

```html
<!DOCTYPE html>
<html lang="en">
<head>
<meta charset="utf-8">
<title>Bravolk Promotion Group</title>
<link href="https://fonts.googleapis.com/css2?family=Oswald:wght@300;400;500&family=Lora:ital@1&display=swap" rel="stylesheet">
<style>
:root{
  --page:#e6e6e6;
  --white:#ffffff;
  --panel:#f7f7f7;
  --dark:#252525;
  --nav:#2b2b2b;
  --blue:#2b66b1;
  --ink:#333333;
  --muted:#777777;
  --rule:#dddddd;
  --orange:#e0703a;
  --sky:#d5dee8;
  --skin:#d9c3b4;
}
*{box-sizing:border-box;margin:0;padding:0}
html,body{width:1009px;height:1200px;overflow:hidden}
body{background:var(--page);font-family:Arial,Helvetica,sans-serif;color:var(--ink);position:relative}
.site{position:absolute;left:0;top:0;width:933px;height:1200px;background:var(--white)}
.abs{position:absolute}
.brand{left:19px;top:28px;font-family:'Oswald',sans-serif;font-weight:500;font-size:26px;color:var(--blue);display:flex;align-items:center;gap:10px;line-height:1.1;width:320px}
.brand .mark{width:34px;height:34px;background:var(--blue);flex:none}
.search{left:707px;top:33px;width:196px;height:22px;background:#6a6a6a;color:#ddd;font-size:10px;padding:5px 8px}
.search .go{position:absolute;right:0;top:0;width:22px;height:22px;background:var(--blue)}
.nav{left:14px;top:97px;width:919px;height:36px;background:var(--nav);border-bottom:3px solid var(--blue);display:flex}
.nav a{font-family:'Oswald',sans-serif;font-size:13px;color:#fff;text-decoration:none;padding:0 12px;line-height:33px;border-right:1px solid #444;text-transform:uppercase}
.nav a.on{background:#1a1a1a}
.nav .social{margin-left:auto;display:flex;gap:6px;align-items:center;padding-right:14px}
.nav .social span{width:17px;height:17px;background:#666}
.hero{left:14px;top:133px;width:919px;height:382px;background:linear-gradient(90deg,#f5f6f8 0%,#eef1f4 45%,#e3e8ee 100%)}
.hero-photo{left:460px;top:0;width:459px;height:382px;background:linear-gradient(90deg,rgba(238,241,244,0) 0%,var(--sky) 30%,var(--skin) 60%,#c8d6e6 100%)}
.hero h1{left:87px;top:108px;font-family:'Oswald',sans-serif;font-weight:400;font-size:33px;color:#3a3a3a;line-height:1.2}
.hero h1 strong{display:block;font-weight:400;font-size:42px;color:var(--blue);margin-left:16px}
.thumb{top:274px;width:190px;height:69px;background:rgba(255,255,255,.88);font-family:'Oswald',sans-serif;font-size:14px;text-align:center;padding-top:18px;color:#333;line-height:1.25}
.thumb b{display:block;font-weight:400;color:var(--blue);font-size:15px}
.arrow{top:300px;width:16px;height:16px;border-radius:50%;background:rgba(255,255,255,.7)}
.content{left:14px;top:515px;width:919px;height:505px;background:var(--panel)}
.welcome{left:45px;top:534px;font-family:'Oswald',sans-serif;font-size:22px;font-weight:400;color:#333}
.rule{left:45px;top:573px;width:634px;height:1px;background:#ccc}
.col{top:597px;width:193px}
.col .pic{width:193px;height:143px;background:linear-gradient(135deg,#eef0f2 0%,#dfe4ea 55%,#d6cdc6 100%)}
.col h2{font-family:'Oswald',sans-serif;font-weight:400;font-size:21px;color:var(--blue);margin-top:30px;line-height:1.1}
.col h3{font-family:'Oswald',sans-serif;font-weight:400;font-size:14px;color:#333;margin-bottom:14px}
.col li{list-style:none;font-size:10px;color:#777;border-bottom:1px solid var(--rule);height:27px;line-height:26px;padding-left:10px}
.col li::before{content:"→";color:var(--orange);margin-right:10px}
.col li:last-child{border-bottom:none}
.btn{display:inline-block;background:var(--blue);color:#fff;font-size:11px;padding:7px 11px;margin-top:21px}
.chat{left:712px;top:539px;width:189px;height:165px;background:#a9a9a9;color:#fff;padding:12px 16px}
.chat .pic{position:absolute;right:0;top:0;width:95px;height:165px;background:linear-gradient(90deg,#a9a9a9,#e9e6e3 45%)}
.chat .q{font-size:14px}
.chat .big{font-size:38px;line-height:.9;letter-spacing:-1px}
.chat .live{font-size:17px}
.chat .hrs{font-size:10px;color:#eee;margin-top:6px}
.chat .cta{position:absolute;left:16px;top:123px;background:#333;font-size:11px;padding:7px 10px}
.quote{left:712px;top:736px;width:189px;height:131px;background:var(--blue);color:#fff;padding:18px 18px}
.quote .mk{font-family:'Lora',serif;font-size:48px;line-height:.6;height:26px}
.quote p{font-family:'Lora',serif;font-style:italic;font-size:12px;line-height:1.45}
.footer{left:14px;top:1020px;width:919px;height:167px;background:var(--dark)}
.fcol{top:1048px;font-family:'Oswald',sans-serif;font-size:14px;color:#fff;line-height:1.25}
.fcol p{font-family:Arial,sans-serif;font-size:10px;color:#777;margin-top:12px;line-height:1.6}
.fcol .phone{font-family:Arial,sans-serif;font-size:17px;color:var(--blue);margin-top:12px}
.fcol a{color:#888;font-family:Arial,sans-serif;font-size:10px;text-decoration:underline}
.ficons{display:flex;gap:9px;margin-top:14px}
.ficons span{width:17px;height:17px;background:#555}
.frule{left:45px;top:1144px;width:856px;height:1px;background:#3a3a3a}
.copy{left:45px;top:1154px;font-size:10px;color:#666}
.top{left:969px;top:1164px;width:40px;height:21px;background:#333;color:#fff;font-size:10px;padding:5px 0 0 6px}
</style>
</head>
<body>
<div class="site">
  <div class="abs brand"><span class="mark"></span>Bravolk Promotion Group</div>
  <div class="abs search">Search<span class="go"></span></div>

  <nav class="abs nav">
    <a class="on">Home</a><a>About Us</a><a>Products</a><a>Networks</a><a>Effectiveness</a><a>Campaigns</a><a>Become a Partner</a><a>Contact Us</a>
    <div class="social"><span></span><span></span><span></span><span></span></div>
  </nav>

  <section class="abs hero">
    <div class="abs hero-photo" role="img" aria-label="Photo of a smiling man in a striped shirt"></div>
    <h1 class="abs">Everything Starts With a<strong>GREAT SOLUTIONS</strong></h1>
    <div class="abs arrow" style="left:8px"></div>
    <div class="abs arrow" style="left:895px"></div>
    <div class="abs thumb" style="left:43px">Everything Starts With a<b>GREAT SOLUTIONS</b></div>
    <div class="abs thumb" style="left:257px">Innovative Ways<b>PERFECT RESULTS!</b></div>
    <div class="abs thumb" style="left:471px">a Driving Force<b>IN YOUR BUSINESS</b></div>
    <div class="abs thumb" style="left:685px">The One and Only the Best<b>ADVERTISING COMPANY</b></div>
  </section>

  <section class="abs content"></section>
  <h2 class="abs welcome">Welcome to Bravolk Promotion!</h2>
  <div class="abs rule"></div>

  <div class="abs col" style="left:45px">
    <div class="pic" role="img" aria-label="Photo of a man working on a laptop"></div>
    <h2>Lorem ipsum</h2><h3>Lorem ipsum</h3>
    <ul><li>Lorem ipsum</li><li>Lorem ipsum</li><li>Lorem ipsum</li><li>Lorem ipsum</li></ul>
    <span class="btn">Click to Call Now!</span>
  </div>
  <div class="abs col" style="left:264px">
    <div class="pic" role="img" aria-label="Photo of women in an office"></div>
    <h2>Lorem ipsum</h2><h3>Lorem ipsum</h3>
    <ul><li>Lorem ipsum Lorem ipsum</li><li>Lorem ipsum</li><li>Lorem ipsum</li><li>Lorem ipsum</li></ul>
    <span class="btn">Click to Call Now!</span>
  </div>
  <div class="abs col" style="left:483px">
    <div class="pic" role="img" aria-label="Photo of a businesswoman with colleagues"></div>
    <h2>Lorem ipsum</h2><h3>Lorem ipsum</h3>
    <ul><li>Lorem ipsum Lorem ipsum</li><li>Lorem ipsum</li><li>Lorem ipsum Lorem ipsum</li><li>Lorem ipsum</li></ul>
    <span class="btn">Click to Call Now!</span>
  </div>

  <aside class="abs chat">
    <div class="pic" role="img" aria-label="Photo of a support agent with a headset"></div>
    <div class="abs" style="left:16px;top:12px">
      <div class="q">Questions?</div><div class="big">Chat</div><div class="live">With us live!</div><div class="hrs">Mon-Fri 8am-9pm</div>
    </div>
    <span class="cta">Click Here!</span>
  </aside>
  <aside class="abs quote">
    <div class="mk">&ldquo;</div>
    <p>Proin nonummy, lacus eget pulvinar lacinia, pede felis dignissim leo, vitae tristique.</p>
  </aside>

  <footer class="abs footer"></footer>
  <div class="abs fcol" style="left:45px;width:190px">For Immediate Onsite or Remote Support:<div class="phone">Call: +0 (321) 5550-184</div></div>
  <div class="abs fcol" style="left:267px;width:190px">Address Info:<p>Lorem ipsum dolor sit amet, consectetur adipisicing elit, sed do eiusmod tempor.</p></div>
  <div class="abs fcol" style="left:487px;width:200px">Email:<p><a>Testmail@bravolkpromotion.ca</a></p></div>
  <div class="abs fcol" style="left:709px">Follow Us:<div class="ficons"><span></span><span></span><span></span><span></span></div></div>
  <div class="abs frule"></div>
  <div class="abs copy">Copyright © 2012. Bravolk Promotion. All rights reserved</div>
</div>
<div class="abs top">&#94; Top</div>
</body>
</html>
```